Willow Dental Business Card

We need business cards for our dental office.
We are looking for a clean, elegant design

We provide dental services to children.
Our card needs to be appealing to referring dentists, parents and our team

Target Market(s)

referring dentists, parents and our team

Industry/Entity Type

Dental Clinic

Contact Information for Business Card

4856 Fenwick Lane, Suite 100
Middleburg Heights, OH 44187

216-382-7461 Voice
216-382-7469 fax
info@willowdentalco.com email
www.willowdentalco.com web

Font styles to use
Sans Serif

Requirements
Must have
• White background - clean, crisp, elegant, simple
• rounded corners
• different color palate - once we come up with design, we will replace the blue with orange, green,
Nice to have
• Follow our logo typeface and colors
• then we can replace color

```html
<!DOCTYPE html>
<html lang="en">
<head>
<meta charset="utf-8">
<title>Willow Dental Business Card</title>
<link rel="stylesheet" href="https://fonts.googleapis.com/css2?family=Nunito:wght@800&family=Open+Sans:wght@400;600&display=swap">
<style>
  :root {
    --brand-green: #0f8241;
    --ink-grey: #6b6b6b;
    --paper: #ffffff;
    --backdrop: #e9eaeb;
  }
  * { box-sizing: border-box; margin: 0; padding: 0; }
  html, body { width: 1200px; height: 900px; overflow: hidden; }
  body {
    background: var(--backdrop);
    font-family: "Open Sans", sans-serif;
    display: flex;
    flex-direction: column;
    align-items: center;
    justify-content: center;
    gap: 56px;
  }
  .card {
    width: 630px;
    height: 360px;
    border-radius: 18px;
    position: relative;
    overflow: hidden;
    box-shadow: 0 6px 18px rgba(0,0,0,0.12);
  }
  .card-front {
    background: var(--brand-green);
    display: flex;
    align-items: center;
    justify-content: center;
  }
  .wordmark {
    font-family: "Open Sans", sans-serif;
    font-weight: 600;
    display: flex;
    align-items: center;
    gap: 14px;
    letter-spacing: 0.5px;
  }
  .card-front .wordmark { color: var(--paper); font-size: 50px; }
  .wordmark-dot {
    width: 18px; height: 18px; border-radius: 50%;
    background: currentColor;
  }
  .card-back { background: var(--paper); }
  .card-back .wordmark {
    position: absolute;
    right: 44px;
    top: 118px;
    color: var(--brand-green);
    font-size: 32px;
  }
  .contact-block {
    position: absolute;
    left: 48px;
    bottom: 38px;
    color: var(--ink-grey);
    font-size: 13.5px;
    line-height: 1.5;
  }
  .person-name {
    font-family: "Nunito", sans-serif;
    font-weight: 800;
    color: var(--brand-green);
    font-size: 21px;
    line-height: 1.2;
  }
  .person-role { font-size: 15px; color: var(--ink-grey); }
  .role-rule {
    width: 72px; height: 2px; background: var(--brand-green);
    margin: 6px 0 22px;
  }
  .address { margin-bottom: 14px; }
  .contact-list { list-style: none; }
  .contact-list li { display: flex; align-items: center; gap: 10px; }
  .contact-list svg { width: 13px; height: 13px; fill: var(--brand-green); flex: none; }
  .web-domain { color: var(--brand-green); }
</style>
</head>
<body>
  <section class="card card-front">
    <div class="wordmark"><span class="wordmark-dot"></span>Willow Dental</div>
  </section>

  <section class="card card-back">
    <div class="wordmark"><span class="wordmark-dot"></span>Willow Dental</div>

    <div class="contact-block">
      <p class="person-name">Lena Marlow</p>
      <p class="person-role">Doctor</p>
      <div class="role-rule"></div>
      <p class="address">4856 Fenwick Lane, Suite 100<br>Middleburg Heights, OH 44187</p>
      <ul class="contact-list">
        <li>
          <svg viewBox="0 0 24 24" aria-hidden="true"><path d="M6.6 10.8a15.1 15.1 0 0 0 6.6 6.6l2.2-2.2a1 1 0 0 1 1-.25 11.4 11.4 0 0 0 3.6.57 1 1 0 0 1 1 1V20a1 1 0 0 1-1 1A17 17 0 0 1 3 4a1 1 0 0 1 1-1h3.5a1 1 0 0 1 1 1c0 1.25.2 2.45.57 3.57a1 1 0 0 1-.25 1z"/></svg>
          216-382-7461
        </li>
        <li>
          <svg viewBox="0 0 24 24" aria-hidden="true"><path d="M6 2h12v5H6zM3 8h18a1 1 0 0 1 1 1v8h-4v5H6v-5H2V9a1 1 0 0 1 1-1zm5 8v4h8v-4z"/></svg>
          216-382-7469
        </li>
        <li>
          <svg viewBox="0 0 24 24" aria-hidden="true"><path d="M2 5h20v14H2zm2 2v.5l8 5 8-5V7z"/></svg>
          info@willowdentalco.com
        </li>
        <li>
          <svg viewBox="0 0 24 24" aria-hidden="true"><circle cx="12" cy="12" r="10"/></svg>
          <span>www.<span class="web-domain">willowdentalco.com</span></span>
        </li>
      </ul>
    </div>
  </section>
</body>
</html>
```